Morning Harbor Bible Fellowship needs a new Business Card/Letterhead Suite

***** IT DOES NOT HAVE TO FEATURE GREEN AND BROWN in order to be a successful design*****

****FONTS: SF New Republic, 'Morning Harbor'; Nexa Light, 'Bible Fellowship'****

***We have two locations, with two addresses. So the business card AND letterhead need to include two sets of address information***

We are a growing church in New York in need of a new stationary suite. We have recently adopted a new logo (via a successful ArtHivePro project) and need new business cards, letterhead, envelopes, and folders.

We would like to see creative, original designs that are modern and clean/elegant (NOT dated "churchy" graphics that are cheesy).

We need this project worked on immediately, as we need to print new business cards for upcoming programs we have on our schedule. So, the designs need to be solid so that we can move quickly throughout the revision process toward print.

We'd also need editables files, so that we can drop in other staff members names/phone numbers, to be able to print cards for those staff needing them.

Requirements
Must have
• Our logo
• Must be given to us in an editable format (to change names)
Nice to have
• Some examples on grey, or recycled, card stock
• card stock (background) does not have to be white
Should not have
• Any extraneous logo's or symbols

```html
<!DOCTYPE html>
<html lang="en">
<head>
<meta charset="utf-8">
<title>Morning Harbor Bible Fellowship Business Card</title>
<link href="https://fonts.googleapis.com/css2?family=Nunito:wght@300;400;700&display=swap" rel="stylesheet">
<style>
  :root {
    --backdrop: #e4e2de;
    --card-white: #f4f4f3;
    --brand-green: #377634;
    --brand-olive: #686239;
    --text-light: #ffffff;
  }
  html, body {
    margin: 0;
    width: 1200px;
    height: 960px;
    overflow: hidden;
    background: var(--backdrop);
    font-family: 'Nunito', sans-serif;
  }
  .canvas { position: relative; width: 1200px; height: 960px; }
  .card {
    position: absolute;
    width: 600px;
    height: 342px;
    box-shadow: 0 2px 6px rgba(0,0,0,0.25);
    overflow: hidden;
  }
  .card-front { left: 302px; top: 119px; background: var(--card-white); }
  .card-back { left: 300px; top: 498px; background: var(--brand-green); }

  .wordmark {
    position: absolute;
    left: 0; right: 0; top: 88px;
    margin: 0;
    text-align: center;
    color: var(--brand-green);
    font-weight: 400;
  }
  .wordmark-name {
    display: block;
    font-size: 48px;
    line-height: 1;
    letter-spacing: -0.5px;
  }
  .wordmark-tagline {
    display: block;
    margin-top: 8px;
    font-size: 15px;
    line-height: 1;
    letter-spacing: 4px;
    text-transform: uppercase;
  }

  .contact-band {
    position: absolute;
    left: 0; top: 197px;
    width: 600px; height: 116px;
    display: flex;
  }
  .band-identity {
    width: 294px;
    background: var(--brand-green);
    color: var(--text-light);
    text-align: right;
    box-sizing: border-box;
    padding: 13px 22px 0 0;
    font-size: 13px;
    line-height: 17px;
    font-weight: 300;
  }
  .band-identity .person-name {
    font-weight: 700;
    font-size: 19px;
    line-height: 22px;
    letter-spacing: 0.3px;
  }
  .band-identity .person-title {
    font-size: 14px;
    line-height: 19px;
    margin-bottom: 3px;
  }
  .band-divider { width: 4px; background: var(--card-white); }
  .band-details {
    flex: 1;
    background: var(--brand-olive);
    color: var(--text-light);
    box-sizing: border-box;
    padding: 16px 0 0 20px;
    font-size: 15px;
    font-weight: 300;
  }
  .detail-row {
    display: flex;
    align-items: center;
    height: 19.5px;
  }
  .detail-row svg { width: 13px; height: 13px; margin-right: 8px; fill: var(--text-light); }

  .back-wordmark {
    position: absolute;
    left: 0; right: 0; top: 128px;
    margin: 0;
    text-align: center;
    color: var(--text-light);
    font-weight: 400;
  }
  .back-wordmark .wordmark-name { font-size: 36px; }
  .back-wordmark .wordmark-tagline { font-size: 13px; margin-top: 8px; }
  .back-web {
    position: absolute;
    left: 0; right: 0; top: 290px;
    text-align: center;
    color: var(--text-light);
    font-weight: 700;
    font-size: 14px;
    letter-spacing: 2.6px;
  }
</style>
</head>
<body>
<div class="canvas">
  <section class="card card-front">
    <h1 class="wordmark">
      <span class="wordmark-name">Morning Harbor</span>
      <span class="wordmark-tagline">Bible Fellowship</span>
    </h1>
    <div class="contact-band">
      <div class="band-identity">
        <div class="person-name">DANIEL REYES</div>
        <div class="person-title">CEO/FOUNDER</div>
        <div>1420 Harbor View Road, Portland, ME 04101</div>
        <div>88 Quay Street, Bath, ME 04530</div>
      </div>
      <div class="band-divider"></div>
      <div class="band-details">
        <div class="detail-row">
          <svg viewBox="0 0 16 16"><path d="M3.5 1l2.5 3-1.5 2c1 2 3 4 5 5l2-1.5 3 2.5-1.5 2.5C7 15 1 9 1 2.5z"/></svg>
          555 214 7730
        </div>
        <div class="detail-row">
          <svg viewBox="0 0 16 16"><path d="M4 0h8v16H4zM5.5 2v10h5V2zM7 13.3h2v1.4H7z" fill-rule="evenodd"/></svg>
          555 318 4402
        </div>
        <div class="detail-row">
          <svg viewBox="0 0 16 16"><path d="M1 3.5h14v9H1zM1.5 4l6.5 5 6.5-5v1L8 10 1.5 5z"/></svg>
          name@morningharbor.com
        </div>
        <div class="detail-row">
          <svg viewBox="0 0 16 16"><circle cx="8" cy="8" r="7"/><path d="M4 4c2 1 2 3 4 3s1 3 3 4c-1 2-4 1-5-1S3 7 4 4z" fill="#686239"/></svg>
          www.morningharbor.com
        </div>
      </div>
    </div>
  </section>

  <section class="card card-back">
    <h2 class="back-wordmark">
      <span class="wordmark-name">Morning Harbor</span>
      <span class="wordmark-tagline">Bible Fellowship</span>
    </h2>
    <div class="back-web">www.morningharbor.com</div>
  </section>
</div>
</body>
</html>
```